We need to a website for a contact center that provides answering services by voice and chat.

A similar website in terms of design is the following site:
http://www.brindlequay.example/

The colors and look and feel should be different and creative but the structure should be similar to the above mentioned website.

Attached is the text file.

The design should communicate professionalism and friendly customer service oriented company. The visitor to the site must have a feel that "this company looks professional and they will take care of my client."

I am looking for design only, but if the designer will also do the coding, it will be an advantage.

Target Market(s)

Our target market are lawyers and doctors who require someone to answer their clients calls 24/7.

Industry/Entity Type

It Company

Requirements
Nice to have
• Since the company is based in Dubai, the website should reflect the Middle East people not pure European or pure Asians. A mixture of nationalities is fine to be visible in the pictures but it must include at least an arab or middle eastern person.
Should not have
• No old style, Times Roman font, do not include illustrations or cartoon graphics or pictures that are very common or widely used.

```html
<!DOCTYPE html>
<html lang="en">
<head>
<meta charset="utf-8">
<title>Palmcrest Group – Call Center &amp; Live Answering</title>
<link href="https://fonts.googleapis.com/css2?family=Cabin:wght@400;500;600&display=swap" rel="stylesheet">
<style>
  :root{
    --bg-red:#9a2d24;
    --bg-red-light:#b0463a;
    --brand:#9b2620;
    --brand-bright:#c0392b;
    --ink:#333;
    --muted:#555;
    --panel:#ffffff;
    --nav:#2b2b2b;
    --card-top:#6a6a6a;
    --card-bottom:#4a4a4a;
    --footer:#1d1d1d;
  }
  *{box-sizing:border-box;margin:0;padding:0}
  html,body{width:929px;height:1200px;overflow:hidden}
  body{
    position:relative;
    font-family:"Cabin",sans-serif;
    color:var(--ink);
    background:radial-gradient(ellipse at 30% 40%,var(--bg-red-light) 0%,var(--bg-red) 70%);
  }
  .utility{position:absolute;top:9px;right:97px;font-size:11px;color:#fff;display:flex;gap:6px;align-items:center}
  .utility .dot{width:12px;height:7px;border-radius:50%;background:#f2c200;display:inline-block;margin-right:4px}
  .page{position:absolute;left:93px;top:30px;width:743px;height:1138px;background:var(--panel);border-radius:3px 3px 0 0}
  .brand{position:absolute;left:19px;top:36px;display:flex;align-items:center;gap:8px;font-size:22px;font-weight:600;color:#333;letter-spacing:.5px}
  .brand .mark{width:14px;height:14px;background:var(--brand);border-radius:50%}
  .search{position:absolute;right:10px;top:14px;width:164px;height:25px;border:1px solid #ddd;display:flex;background:#fafafa}
  .search span{flex:1;font-size:9px;font-style:italic;color:#999;padding:7px 10px}
  .search .btn{width:32px;border-left:1px solid #ddd;display:flex;align-items:center;justify-content:center;background:#f0f0f0}
  .call{position:absolute;right:10px;top:58px;font-size:16px;color:#222;display:flex;align-items:center;gap:5px}
  .call b{font-weight:400;color:var(--brand-bright)}
  .nav{position:absolute;left:8px;top:100px;width:727px;height:38px;background:linear-gradient(#3a3a3a,#1f1f1f);display:flex;align-items:center;font-size:11.5px;color:#fff}
  .nav a{padding:0 14px;color:#fff;text-decoration:none;height:38px;line-height:38px}
  .nav a.active{background:var(--brand);width:89px;text-align:center;font-weight:600;margin-right:8px}
  .hero{position:absolute;left:8px;top:146px;width:726px;height:314px;background:linear-gradient(100deg,#d9dde2 0%,#c4b49f 30%,#e6e0d6 50%,#7d8a96 85%,#5c6570 100%)}
  .hero .arrow{position:absolute;top:144px;width:27px;height:26px;background:#333;display:flex;align-items:center;justify-content:center}
  .trial{position:absolute;left:455px;top:51px;width:214px;height:212px;background:rgba(150,40,35,.88);border-radius:3px;padding:12px 17px}
  .trial h2{font-weight:500;font-size:18px;color:#fff;text-align:center;margin-bottom:10px}
  .trial .field{height:27px;background:#fff;margin-bottom:9px;font-size:9px;font-style:italic;color:#888;padding:8px 10px}
  .trial .go{position:absolute;right:17px;bottom:19px;background:#1e1e1e;color:#fff;font-size:11.5px;padding:7px 15px;border-radius:2px}
  .card{position:absolute;left:9px;width:232px;background:linear-gradient(var(--card-top),var(--card-bottom));color:#fff;border-radius:2px;padding:14px 13px}
  .card h3{font-weight:400;font-size:15px;display:flex;align-items:center;gap:12px}
  .card p{font-size:9.2px;line-height:14px;color:#eee;margin-top:10px}
  .card .more{position:absolute;right:16px;bottom:9px;background:var(--brand-bright);font-size:8.5px;padding:6px 9px;border-radius:2px}
  .email-row{display:flex;margin-top:12px;height:25px;background:#fff;border-radius:2px}
  .email-row span{flex:1;font-size:9px;font-style:italic;color:#888;padding:7px 10px}
  .email-row .send{width:34px;border-left:1px solid #ddd;display:flex;align-items:center;justify-content:center}
  .social{display:flex;gap:3px;margin-top:10px}
  .social i{width:31px;height:31px;border-radius:50%;background:#c9c9c9;display:flex;align-items:center;justify-content:center}
  .content{position:absolute;left:266px;top:498px;width:469px}
  .content h1{font-weight:400;font-size:18px;color:var(--brand);margin-bottom:14px}
  .content p{font-size:9.2px;line-height:15.5px;color:var(--muted);padding-left:3px;margin-bottom:6px}
  .content h4{font-weight:400;font-style:italic;font-size:13px;color:var(--brand-bright);margin:7px 0 2px 3px}
  .benefits{list-style:none;padding-left:3px;margin-bottom:4px}
  .benefits li{font-size:9.2px;line-height:19.3px;color:var(--muted);padding-left:19px;position:relative}
  .benefits li::before{content:"›";position:absolute;left:2px;top:-1px;color:var(--brand);font-weight:600;font-size:13px}
  .cta{font-size:13.5px;line-height:18px;color:var(--brand-bright);margin:12px 0 0 3px}
  .cta b{color:#111;font-weight:500}
  .footer{position:absolute;left:0;top:1040px;width:743px;height:98px;background:var(--footer);color:#fff;text-align:center}
  .footer nav{font-size:10.5px;margin-top:22px;word-spacing:1px}
  .footer nav span{margin:0 5px}
  .footer small{display:block;font-size:10px;margin-top:15px}
  .footer small em{font-style:normal;color:#e0473a}
</style>
</head>
<body>
  <div class="utility">FAQ <span>|</span> Support <span>|</span> <span><i class="dot"></i>Live Chat</span></div>

  <div class="page">
    <div class="brand"><span class="mark"></span>Palmcrest Group</div>

    <div class="search"><span>Search...</span>
      <div class="btn"><svg width="16" height="16" viewBox="0 0 16 16"><circle cx="6.5" cy="6.5" r="4.5" fill="none" stroke="#9b2620" stroke-width="2"/><line x1="10" y1="10" x2="14.5" y2="14.5" stroke="#9b2620" stroke-width="2.5"/></svg></div>
    </div>
    <div class="call"><svg width="14" height="14" viewBox="0 0 14 14"><path d="M3 1l2.5 3-1.5 1.5c.8 1.8 2 3 3.8 3.8L9.3 7.8l3 2.5-1.5 2.5C6 12.5 1.5 8 1 3z" fill="#e0701e"/></svg>Call Us: <b>+971 4 555 0182</b></div>

    <nav class="nav">
      <a class="active">Home</a><a>About the Group</a><a>Division</a><a>Group Companies</a><a>Press Room</a><a>Employment &amp; Association</a><a>Contact Us</a>
    </nav>

    <section class="hero" role="img" aria-label="Photo of smiling call center agents wearing headsets in a bright office">
      <div class="arrow" style="left:0"><svg width="8" height="10"><path d="M6 1L2 5l4 4" stroke="#fff" fill="none"/></svg></div>
      <div class="arrow" style="right:0"><svg width="8" height="10"><path d="M2 1l4 4-4 4" stroke="#fff" fill="none"/></svg></div>
      <form class="trial">
        <h2>Get 14 Day Free Trial</h2>
        <div class="field">Name</div>
        <div class="field">Contact No.</div>
        <div class="field">Email Address</div>
        <div class="go">GET STARTED</div>
      </form>
    </section>

    <aside>
      <div class="card" style="top:498px;height:138px">
        <h3><svg width="38" height="30" viewBox="0 0 38 30"><circle cx="13" cy="17" r="9" fill="none" stroke="#fff" stroke-width="5" stroke-dasharray="3.5 2.3"/><circle cx="13" cy="17" r="3" fill="#fff"/><circle cx="30" cy="7" r="4" fill="none" stroke="#ddd" stroke-width="3" stroke-dasharray="2 1.5"/></svg>How it Works</h3>
        <p>Palmcrest Telecom takes pride in ensuring that your calls are handled in the most professional manner. We offer real solutions for lawyers seeking to improve</p>
        <span class="more">READ MORE</span>
      </div>
      <div class="card" style="top:648px;height:137px">
        <h3><svg width="32" height="32" viewBox="0 0 32 32"><rect x="2" y="6" width="24" height="24" fill="none" stroke="#fff" stroke-width="2.5"/><path d="M10 21l3 0 16-16-3-3-16 16z" fill="#fff"/></svg>Request Pricing</h3>
        <p>Our prices are based on the actual agent talk time and the duration for which the services are availed. Our economical costs ensure that your monthly rate.</p>
        <span class="more">READ MORE</span>
      </div>
      <div class="card" style="top:798px;height:110px;padding-top:8px">
        <h3 style="align-items:flex-start"><svg width="34" height="34" viewBox="0 0 34 34"><path d="M2 14L17 3l15 11v17H2z" fill="#f0a020"/><path d="M2 14l15 11 15-11" fill="#ffd24a" stroke="#e08a10"/></svg><span>Newsletter Sign up<br><small style="font-size:9.2px;color:#eee;line-height:14px;display:block;margin-top:6px">Sign up for our FREE Monthly Newsletter</small></span></h3>
        <div class="email-row"><span>Enter your Email...</span><div class="send"><svg width="14" height="10"><path d="M1 1l4 4-4 4M7 1l4 4-4 4" stroke="#9b2620" stroke-width="2" fill="none"/></svg></div></div>
      </div>
      <div class="card" style="top:922px;height:86px">
        <h3>Get it Touch</h3>
        <div class="social">
          <i><svg width="18" height="13"><rect x="1" y="1" width="16" height="11" fill="none" stroke="#fff" stroke-width="1.5"/><path d="M1 1l8 6 8-6" stroke="#fff" fill="none" stroke-width="1.5"/></svg></i><i></i><i></i><i></i><i></i>
        </div>
      </div>
    </aside>

    <main class="content">
      <h1>Welcome to Palmcrest Group</h1>
      <p>Palmcrest Telecom is a24/7 call center and live answering service, we provide customized solutions for small, medium, and large organizations. Our customized solutions help our clients get the maximum return on their investment by capturing more leads and projecting a professional image to their customers, in addition tohuge savings on overhead and labor costs.</p>
      <h4>10 Ways Your Company Can Benefit:</h4>
      <ul class="benefits">
        <li>Capture more business &amp; increase profits.</li>
        <li>Save thousands on labor costs.</li>
        <li>Improve your company’s "phone image".</li>
        <li>Streamline your call flow.</li>
        <li>Conduct business 24/7 without the overhead.</li>
        <li>Take advantage of a turn-key, streamlined solution.</li>
        <li>Respond instantaneously to clients and prospects.</li>
        <li>Palmcrest Telecom uses the most reliable equipment in the industry.</li>
        <li>Palmcrest Telecom selects the right people with the best voices.</li>
        <li>Palmcrest Telecom over-staffs receptionists to minimize hold times.</li>
      </ul>
      <p>At Palmcrest Telecom, we customize our services to each client’s specific needs. We do not provide a "one size fits all" solutions. We take pride in developing solutions to fit the specific requirements of our clients’ individual situation and needs.</p>
      <p>We employ the right people with the best voices and over-staff our team of live receptionists to minimize hold times. Our team of experts has experience spanning decades and cutting across industries to provide our customers with the right solution for their niche area of operation.</p>
      <p class="cta">For more information or to speak with an account specialist, please call Palmcrest Telecom at <b>+9714-555-0182!</b></p>
    </main>

    <footer class="footer">
      <nav>Home<span>|</span>About the Group Divisions<span>|</span>Group Companies<span>|</span>Press Room<span>|</span>Employment &amp; Association<span>|</span>Contact Us</nav>
      <small>Copyright © 2013 <em>Palmcrest Group</em>. All right reserved.</small>
    </footer>
  </div>
</body>
</html>
```